Wine Label for a White and a Red Wine from Italy

We have a very good idea of what we want with artwork. We need you to please design a 'template' with the text so we can change out the artwork from year to year. Samples are shown of what we are looking for. We are looking for options with the two basic designs. Brand name of wine is: Valora di Castegno. Both wines are in a light green Bordeaux-style bottle (note: we don't show a light green bottle in the mockup but please remember the bottle is light green). Artwork is provided. We'd like to see either the green or blue butterfly on the white wine, the red butterfly is for the red wine. Please base the design on the attached label from Brailey and/or the attached label from Chateau Mervanges.

Target Market(s)

Millennials, women

Requirements
Must have
• The artwork (butterflies) attached.
Nice to have
• Elegant, readable fonts. Please make the text so it can be changed by the printer. Please make it so the artwork can be changed too.

```html
<!DOCTYPE html>
<html lang="en">
<head>
<meta charset="utf-8">
<title>Valora di Castegno – Rosso Label</title>
<link rel="stylesheet" href="https://fonts.googleapis.com/css2?family=Noto+Serif:wght@300;400&family=Roboto+Condensed:wght@400&family=Source+Serif+4:opsz,wght@8..60,400&display=swap">
<style>
  :root {
    --backdrop: #d6d6d6;
    --paper: #f5f5f3;
    --sun-yellow: #ecc862;
    --sun-yellow-deep: #e2b64a;
    --artwork-tone: #dcab45;
    --ink: #3b3b3b;
    --ink-soft: #555555;
  }
  * { margin: 0; padding: 0; box-sizing: border-box; }
  html, body {
    width: 714px;
    height: 1200px;
    overflow: hidden;
    background: var(--backdrop);
  }
  .canvas {
    position: relative;
    width: 714px;
    height: 1200px;
  }
  .label {
    position: absolute;
    left: 57px;
    top: 111px;
    width: 600px;
    height: 977px;
    background: var(--paper);
    overflow: hidden;
    box-shadow: 0 2px 8px rgba(0,0,0,0.12);
  }
  .label__band {
    position: absolute;
    left: 0;
    top: 0;
    width: 600px;
    height: 300px;
  }
  .label__artwork {
    position: absolute;
    left: 97px;
    top: 40px;
    width: 406px;
    height: 356px;
  }
  .label__text {
    position: absolute;
    left: 0;
    width: 100%;
    text-align: center;
    line-height: 1;
    color: var(--ink);
    font-weight: 400;
  }
  .brand-name {
    top: 412px;
    font-family: "Noto Serif", serif;
    font-weight: 300;
    font-size: 84px;
    color: var(--ink-soft);
    letter-spacing: -1px;
  }
  .brand-sub {
    top: 498px;
    font-family: "Noto Serif", serif;
    font-weight: 300;
    font-size: 30px;
    color: var(--ink-soft);
  }
  .cuvee {
    top: 627px;
    font-family: "Roboto Condensed", sans-serif;
    font-size: 27px;
    letter-spacing: 0.5px;
  }
  .vintage {
    top: 696px;
    font-family: "Source Serif 4", serif;
    font-size: 24px;
  }
  .varietal {
    top: 736px;
    font-family: "Noto Serif", serif;
    font-size: 38px;
  }
  .region {
    top: 776px;
    font-family: "Source Serif 4", serif;
    font-size: 28px;
  }
  .producer {
    top: 840px;
    font-family: "Source Serif 4", serif;
    font-size: 21px;
    letter-spacing: -0.4px;
  }
  .farming {
    top: 889px;
    font-family: "Source Serif 4", serif;
    font-size: 21px;
  }
</style>
</head>
<body>
<main class="canvas">
  <section class="label">
    <svg class="label__band" viewBox="0 0 600 300" aria-hidden="true">
      <defs>
        <linearGradient id="bandFade" x1="0" y1="0" x2="0" y2="1">
          <stop offset="0" stop-color="var(--sun-yellow)"/>
          <stop offset="1" stop-color="var(--sun-yellow-deep)"/>
        </linearGradient>
      </defs>
      <path d="M0 0 H600 V270 C560 274 520 262 480 274 C430 286 380 268 330 278 C280 288 240 270 190 280 C140 290 100 268 60 278 C35 284 15 274 0 280 Z" fill="url(#bandFade)"/>
    </svg>
    <svg class="label__artwork" viewBox="0 0 406 356" role="img" aria-label="Artwork placeholder: painted butterfly on an ochre brushstroke circle, changed each vintage">
      <ellipse cx="203" cy="178" rx="200" ry="175" fill="var(--artwork-tone)"/>
    </svg>

    <h1 class="label__text brand-name">Valora</h1>
    <p class="label__text brand-sub">di Castegno</p>
    <p class="label__text cuvee">BARREL SELECT</p>
    <p class="label__text vintage">2018</p>
    <p class="label__text varietal">Rosso</p>
    <p class="label__text region">Piemonte, Italy</p>
    <p class="label__text producer">Artisanlly Crafted by Cantina Sette Colli</p>
    <p class="label__text farming">sustainably farmed</p>
  </section>
</main>
</body>
</html>
```